Postcard Design

We are a yoga business that has a training called:
QUIET HORIZON-empowering educators and parents to give children and youth the gift of yoga and meditation as a tool for life. (We would like this description and the text below included in the postcard)

3-day training for educators and parents at our facility or yours.

You will leave equipped to teach mindful breathing techniques, meditation, and a yoga based sequence to revitalize the body. You will have the tools to empower your students to be confident and appreciate their mind-body connection.

**Training is designed for a minimum of 3 and a maximum of 15 educators and parents from the same organization.

FOR PRICING AND BOOKING :Wenda Falkirk 555-310-2769
wfalkirk@brightlarkstudio.com

(Not to be included in design) We are using these postcards for a conference where teachers and school administrators go to find new things for their schools and students.
Updates

I thought I had uploaded our logo! so sorry but I made sure and saved it now I would like it on the design. Thank you.

Target Market(s)

Educators and parents of all age groups

Industry/Entity Type

Training

Font styles to use
Sans Serif

Requirements
Must have
• Pleas take out Copper Thistle logo (that is not our logo, but it is our picture and it is us in it) our logo is uploaded and we would like it to be used. Thank you.
Nice to have
• If possible use the pic I uploaded and take out the copper thistle logo and put QUIET HORIZON or our logo, also uploaded. This picture is of my son, husband, and I so we own it.
Should not have
• Corny yoga pictures or people dressed in all white.

```html
<!DOCTYPE html>
<html lang="en">
<head>
<meta charset="utf-8">
<title>Quiet Horizon Postcard</title>
<link rel="stylesheet" href="https://fonts.googleapis.com/css2?family=Arimo:wght@400&display=swap">
<style>
  :root {
    --page-bg: #e6e8e7;
    --card-bg: #f7f7f6;
    --ink: #2b2b2b;
    --navy: #17224d;
    --rule: #8a8a8a;
    --sky-blue: #5bbfe3;
    --stamp-line: #7d7d7d;
  }
  * { margin: 0; padding: 0; box-sizing: border-box; }
  html, body {
    width: 1200px; height: 800px; overflow: hidden;
    background: var(--page-bg);
    font-family: "Arimo", Arial, sans-serif;
    color: var(--ink);
  }
  .postcard {
    position: absolute; left: 90px; top: 56px;
    width: 1020px; height: 688px;
    background: var(--card-bg);
    box-shadow: 0 6px 24px rgba(0,0,0,0.12);
    overflow: hidden;
  }
  .brand-circle {
    position: absolute; left: 34px; top: 38px;
    width: 176px; height: 176px; border-radius: 50%;
    background: var(--navy);
    display: flex; align-items: center; justify-content: center;
    text-align: center;
  }
  .brand-circle__name {
    color: #fff; font-size: 19px; line-height: 1.25; letter-spacing: 1px;
  }
  .program {
    position: absolute; left: 222px; top: 112px; width: 264px;
    text-align: center; color: var(--navy);
  }
  .program__name { font-size: 19px; letter-spacing: 1px; }
  .program__tagline {
    margin-top: 8px; font-size: 12.5px; line-height: 16px;
  }
  .copy {
    position: absolute; left: 22px; top: 236px; width: 460px;
    font-size: 18px; line-height: 22px;
  }
  .copy p { margin-bottom: 10px; }
  .copy .note { margin-top: 18px; }
  .booking {
    position: absolute; left: 22px; top: 572px;
    font-size: 17px; line-height: 24px;
  }
  .booking__person, .booking__email { padding-left: 12px; }
  .figure-mark {
    position: absolute; left: 378px; top: 564px; width: 104px; height: 72px;
    background: radial-gradient(ellipse at center, var(--sky-blue) 0%, rgba(91,191,227,0.35) 55%, rgba(91,191,227,0) 75%);
  }
  .color-band {
    position: absolute; left: 64px; top: 656px; width: 418px; height: 32px;
    background: linear-gradient(90deg, #e0477a, #f0a33a, #8cc63f, #2aa7a0, #3b5aa6, #7b4a9e, #e04a5a, #2aa7a0);
  }
  .divider {
    position: absolute; left: 493px; top: 34px; bottom: 10px;
    width: 1px; background: var(--rule);
  }
  .stamp-box {
    position: absolute; left: 787px; top: 26px;
    width: 193px; height: 191px;
    border: 1.5px solid var(--stamp-line);
  }
  .address-line {
    position: absolute; left: 556px; width: 366px; height: 1px;
    background: var(--stamp-line);
  }
</style>
</head>
<body>
  <main class="postcard">
    <div class="brand-circle">
      <span class="brand-circle__name">BRIGHT LARK<br>STUDIO</span>
    </div>
    <div class="program">
      <div class="program__name">QUIET HORIZON</div>
      <p class="program__tagline">empowering educators and parents to give children and youth the gift of yoga and meditation as a tool for life</p>
    </div>

    <section class="copy">
      <p>3-day training for educators and parents<br>&nbsp;at our facility or yours.</p>
      <p>You will leave equipped to teach mindful<br>breathing techniques, meditation, and a yoga<br>based sequence to revitalize the body. You will<br>have the tools to empower your students to be<br>confident and appreciate their mind-body<br>connection.</p>
      <p class="note">"Training is designed for a minimum of 3 and a<br>&nbsp;&nbsp;maximum of 15 educators and parents from<br>&nbsp;&nbsp;the same organization.</p>
    </section>

    <section class="booking">
      <div class="booking__label">FOR PRICING AND BOOKING :</div>
      <div class="booking__person">Wenda Falkirk 555-310-2769</div>
      <div class="booking__email">wfalkirk@brightlarkstudio.com</div>
    </section>

    <div class="figure-mark" role="img" aria-label="Light blue silhouette of a person in a standing yoga pose"></div>
    <div class="color-band" role="img" aria-label="Band of multicoloured overlapping triangles"></div>

    <div class="divider"></div>
    <div class="stamp-box"></div>
    <div class="address-line" style="top:419px"></div>
    <div class="address-line" style="top:467px"></div>
    <div class="address-line" style="top:519px"></div>
    <div class="address-line" style="top:569px"></div>
  </main>
</body>
</html>
```